Flyer für unser Jubiläumscamp "herbstcamp"

Am 10. - 14.10.2022 und 17. - 21. 10.2022 organisieren wir je eine Woche ein Fussballcamp für Kinder ab 5 Jahren bis 12 Jahren. Ebenfalls feiern wir unser 5 jähriges Jubiläum und bieten deshalb das Camp für 300 statt 350 CHF an.
Für dieses Camp (mit dieses 2 Angeboten) möchten wir einen speziellen Flyer haben. Der Flyedr sollte Kinder freundlich aber auch modern sein. Wir bieten auch ein Leistungs, Girls Only sowie ein Goalicamp. (eventuell ist dies aber zu überlastet dan)
Infos zu unseren Camps: https://balmokicker.ch/events/2022-sommercamps-juli/

Target Market(s)

Kinder, 5-12 Jahre

Requirements
Must have
• Logo, Fun Kidscamp
Should not have
• Gleiches wie der Flyer angehängt.

```html
<!DOCTYPE html>
<html lang="de">
<head>
<meta charset="utf-8">
<title>Herbstcamp Flyer</title>
<link href="https://fonts.googleapis.com/css2?family=Courgette&family=Roboto+Condensed:wght@300;700&family=Open+Sans:wght@400;700&display=swap" rel="stylesheet">
<style>
  :root {
    --navy: #213a7c;
    --navy-deep: #1b326f;
    --orange: #f0852a;
    --yellow: #f2dc1d;
    --white: #ffffff;
    --page: #eeeeee;
    --sky: #8fb8e6;
    --grass: #4f8a3a;
  }
  * { margin: 0; padding: 0; box-sizing: border-box; }
  html, body { width: 1200px; height: 1200px; overflow: hidden; background: var(--page); }
  .flyer {
    position: absolute; left: 156px; top: 30px;
    width: 887px; height: 1140px;
    background: var(--navy); overflow: hidden;
    font-family: "Open Sans", sans-serif;
  }
  .hero-photo {
    position: absolute; left: 0; top: 0; width: 100%; height: 560px;
    background: linear-gradient(180deg, var(--sky) 0%, #b9d3ef 30%, #6f9c5a 52%, var(--grass) 100%);
  }
  .hero-mascot {
    position: absolute; left: 330px; top: 10px; width: 520px; height: 560px;
    border-radius: 48% 48% 20% 20%;
    background: radial-gradient(ellipse at 50% 45%, #f6d540 0%, #f39a3a 55%, rgba(243,130,40,0) 75%);
  }
  .bands { position: absolute; left: 0; top: 0; width: 100%; height: 100%; }
  .brand {
    position: absolute; left: 61px; top: 110px;
    display: flex; align-items: center; gap: 10px;
  }
  .brand-dot { width: 34px; height: 34px; border-radius: 50%; background: var(--orange); }
  .brand-name { font-weight: 700; font-size: 28px; color: var(--white); }
  .headline {
    position: absolute; left: 0; width: 100%; text-align: center;
    font-family: "Courgette", cursive; line-height: 1;
  }
  .headline-week { top: 452px; font-size: 104px; color: var(--white); }
  .headline-camp { top: 574px; font-size: 104px; color: var(--orange); }
  .dates {
    position: absolute; left: 0; top: 702px; width: 100%; text-align: center;
    font-family: "Roboto Condensed", sans-serif; font-weight: 700;
    font-size: 36px; line-height: 40px; color: var(--white);
  }
  .dates .joiner { font-weight: 300; margin-left: 10px; }
  .age-pill {
    position: absolute; left: 172px; top: 797px; width: 526px; height: 38px;
    border-radius: 19px; background: var(--orange); color: var(--white);
    font-weight: 700; font-size: 26px; line-height: 38px; text-align: center;
  }
  .offer {
    position: absolute; left: 53px; top: 910px; padding-left: 20px;
    border-left: 5px solid var(--orange);
    color: var(--navy); font-weight: 700; font-size: 22.5px; line-height: 32px;
    text-transform: uppercase;
  }
  .features {
    position: absolute; top: 1000px; left: 0; width: 100%;
    list-style: none; color: var(--navy-deep); font-size: 19px; line-height: 26px;
  }
  .features li { position: absolute; padding-left: 30px; }
  .features li:nth-child(1) { left: 61px; }
  .features li:nth-child(2) { left: 490px; }
  .features svg { position: absolute; left: 0; top: 3px; }
  .camp-link {
    position: absolute; left: 0; top: 1092px; width: 100%; text-align: center;
    color: var(--yellow); font-weight: 700; font-size: 19px;
  }
</style>
</head>
<body>
<div class="flyer">
  <div class="hero-photo" role="img" aria-label="Foto: Löwen-Maskottchen winkt auf einem Fussballplatz mit Kindern und Trainer"></div>
  <div class="hero-mascot" role="img" aria-label="Löwen-Maskottchen des Camps"></div>

  <svg class="bands" viewBox="0 0 887 1140" preserveAspectRatio="none" aria-hidden="true">
    <path fill="#213a7c" d="M0 520 L120 508 L300 522 L520 512 L700 520 L887 506 L887 1140 L0 1140 Z"/>
    <path fill="#f2dc1d" d="M0 860 L40 852 L160 866 L260 850 L420 862 L560 848 L700 860 L887 846 L887 1070 L0 1070 Z"/>
    <path fill="#213a7c" d="M0 1060 L150 1052 L330 1064 L520 1054 L720 1066 L887 1056 L887 1140 L0 1140 Z"/>
  </svg>

  <div class="brand">
    <span class="brand-dot"></span>
    <span class="brand-name">Balmo Kicker</span>
  </div>

  <h1 class="headline headline-week">Einwöchiges</h1>
  <h2 class="headline headline-camp">Fußballcamp</h2>

  <p class="dates">10. BIS 14. OKTOBER 2022<span class="joiner">und</span><br>17. BIS 21. OKTOBER 2022</p>

  <p class="age-pill">FÜR KINDER VON 5 BIS 12 JAHREN</p>

  <p class="offer">Auch wir feiern unser 5-jähriges Jubiläum und<br>bieten das Camp daher für CHF 300 statt CHF 350 an.</p>

  <ul class="features">
    <li>
      <svg width="22" height="22" viewBox="0 0 22 22"><circle cx="11" cy="11" r="9" fill="none" stroke="#1b326f" stroke-width="1.8"/><path d="M6.5 11 L10 14.5 L18 5" fill="none" stroke="#1b326f" stroke-width="2" stroke-linecap="round"/></svg>
      Flyedr muss kinderfreundlich,<br>aber modern sein.
    </li>
    <li>
      <svg width="22" height="22" viewBox="0 0 22 22"><circle cx="11" cy="11" r="9" fill="none" stroke="#1b326f" stroke-width="1.8"/><path d="M6.5 11 L10 14.5 L18 5" fill="none" stroke="#1b326f" stroke-width="2" stroke-linecap="round"/></svg>
      Wir bieten eine Performance,<br>Girls only und ein Torcamp an.
    </li>
  </ul>

  <p class="camp-link">balmokicker.ch/events/2022-sommercamps-juli</p>
</div>
</body>
</html>
```